Piano-centered Instrumental Jazz Album Needs Cover Artwork

The cover has five parts, each one has obligatory features:

I. Main cover

1. Title: Gentle Willow II.
2. Artist: Ember Reed Trio
3. Design image*

* The main design motive can be something that suggests the number 4 (quartet), the sun (sunlight, sun rays), music, piano, notes, nature… Can, but doesn’t have to be one or more of these. But it should represent what the title says.
* I prefer zen-like, minimalist solutions.
* NO stock images, please! Except for unrecognizable parts of something.

II. Cover inside

1. Track list (18 songs) with durations
2. All songs written by Bence Morvath
3. Copyright Velmorsound 2016.
4. Design image

III. Disc

1. Artist: Ember Reed Trio
2. Title: Gentle Willow II.
3. All songs written by Bence Morvath (round on the edge)
4. Copyright Velmorsound 2016. (round on the edge)
5. www.velmorsound.com (round on the edge)

IV. Cover back

1. Track list (same as cover inside)
4. www.velmorsound.com
5. design image (optional)
6. The paper of this page is longer than the main cover, because it is to be turned up when put in the CD case, and there is the saddle with the name of the Artist and Title of the album. On both ends.

V. Under the disc

1. No words, only some design feature.

Important:
The main cover I need in RGB and also CMYK, all the others only CMYK.
I need the work file (cdr, ai or whatever you use)
I need the CMYK images prepared for printing (sizes set, and that little extra on the edges).
I need the RGB main cover cover in jpeg, 3000x3000 pixels.
That's all. :)

The most important of these all is of course the main cover RGB. Do this one first!

Here’s a sample to listen, it might inspire you:

https://files.exampleshare.test/u/48301772/ember%20reed%20sample%2020160103.mp3

If you take a closer look at my website, you can see the whole concept.

Good luck and enjoy!
Regards,
Bence

Requirements
Must have
• Tracklist:
• 1 First, in G 05:08
• 2 Second, in Em 05:11
• 3 Third, in G 05:09
• 4 Fourth, in A 05:07
• 5 Fifth, in Bm 05:01
• 6 Sixth, in A 05:11
• 7 Seventh, in G 05:07
• 8 Eighth, in Bm 05:06
• 9 Ninth, in Gm 05:04
• 10 Tenth, in E 05:03
• 11 Eleventh, in G 05:12
• 12 Twelfth, in A 05:09
• 13 Thirteenth, in E 05:10
• 14 Fourteenth, in Am 05:14
• 15 Fifteenth, in F 05:05
• 16 Sixteenth, in Am 05:05
• 17 Seventeenth, in F 05:04
• 18 Eighteenth, in D 05:07
Should not have
• Stock images copy-pasted, additional copyright costs.

```html
<!DOCTYPE html>
<html lang="en">
<head>
<meta charset="utf-8">
<title>Ember Reed Trio – Gentle Willow II</title>
<link rel="stylesheet" href="https://fonts.googleapis.com/css2?family=Fira+Sans:wght@700&family=Satisfy&display=swap">
<style>
  :root {
    --page-bg: #f1f1f1;
    --sun-yellow: #f6ee3c;
    --leaf-lime: #c9dc3a;
    --leaf-green: #8cc63f;
    --leaf-deep: #5fae3a;
    --leaf-shadow: #6fb43a;
    --mist-blue: #8fb3a6;
    --title-white: #ffffff;
  }
  * { margin: 0; padding: 0; box-sizing: border-box; }
  html, body {
    width: 1200px;
    height: 901px;
    overflow: hidden;
    background: var(--page-bg);
  }
  .album-cover {
    position: absolute;
    left: 312px;
    top: 153px;
    width: 624px;
    height: 614px;
    overflow: hidden;
  }
  .cover-artwork {
    position: absolute;
    inset: 0;
    background:
      radial-gradient(ellipse 34% 20% at 30% 6%, rgba(125, 195, 50, 0.95), rgba(125, 195, 50, 0) 100%),
      radial-gradient(ellipse 16% 40% at 10% 45%, rgba(115, 190, 55, 0.95), rgba(115, 190, 55, 0) 100%),
      radial-gradient(ellipse 30% 26% at 52% 28%, rgba(250, 240, 60, 0.95), rgba(250, 240, 60, 0) 100%),
      radial-gradient(ellipse 25% 20% at 60% 50%, rgba(240, 232, 50, 0.8), rgba(240, 232, 50, 0) 100%),
      radial-gradient(ellipse 45% 30% at 12% 100%, var(--mist-blue), rgba(143, 179, 166, 0) 100%),
      radial-gradient(ellipse 40% 28% at 85% 82%, rgba(170, 210, 110, 0.85), rgba(170, 210, 110, 0) 100%),
      linear-gradient(180deg, var(--leaf-lime) 0%, #d8e24a 38%, var(--leaf-green) 72%, var(--leaf-deep) 100%);
  }
  .cover-titles {
    position: absolute;
    left: 125px;
    top: 357px;
  }
  .artist-name {
    font-family: "Fira Sans", "Arial Black", Arial, sans-serif;
    font-weight: 700;
    font-size: 30px;
    letter-spacing: 1.5px;
    color: var(--title-white);
    line-height: 1;
    text-transform: uppercase;
    white-space: nowrap;
  }
  .album-title {
    margin: 14px 0 0 117px;
    font-family: "Satisfy", "Brush Script MT", cursive;
    font-weight: 400;
    font-size: 40px;
    color: var(--title-white);
    line-height: 1;
    white-space: nowrap;
  }
</style>
</head>
<body>
  <main class="album-cover">
    <div class="cover-artwork" role="img" aria-label="Backlit green willow leaves over a soft yellow-green sunlit blur"></div>
    <div class="cover-titles">
      <h1 class="artist-name">Ember Reed Trio</h1>
      <h2 class="album-title">Gentle Willow II</h2>
    </div>
  </main>
</body>
</html>
```